Building Company Business Card Design

I am looking to get a business card designed for my Building Company. Please find the logo attached.

Industry/Entity Type

Business

Contact Information for Business Card

Mobile 0472 913 046
Email admin@tarrowconstructworks.com.au
Website www.tarrowconstructworks.com.au

Colors
0255a3

```html
<!DOCTYPE html>
<html lang="en">
<head>
<meta charset="utf-8">
<title>Tarrow Construct Works – Business Card</title>
<link rel="stylesheet" href="https://fonts.googleapis.com/css2?family=Montserrat:wght@600&family=Open+Sans:wght@400&display=swap">
<style>
  :root {
    --brand-blue: #1558a6;
    --card-white: #ffffff;
    --ink-grey: #4d4f53;
    --page-bg: #2a2a2c;
  }
  * { margin: 0; padding: 0; box-sizing: border-box; }
  html, body { width: 1200px; height: 880px; overflow: hidden; }
  body {
    background: var(--page-bg);
    display: flex;
    align-items: center;
    justify-content: center;
    gap: 40px;
  }
  .card {
    position: relative;
    width: 560px;
    height: 342px;
    background: var(--card-white);
    border-radius: 22px;
    overflow: hidden;
  }
  .card-front__panel {
    position: absolute;
    inset: 0;
    width: 100%;
    height: 100%;
  }
  .wordmark {
    font-family: "Montserrat", sans-serif;
    font-weight: 600;
    text-transform: uppercase;
    line-height: 1.15;
  }
  .card-front .wordmark {
    position: absolute;
    left: 24px;
    top: 112px;
    color: var(--card-white);
    font-size: 22px;
    letter-spacing: 0.02em;
  }
  .card-front .wordmark .wordmark__sub {
    display: block;
    font-size: 10px;
    letter-spacing: 0.3em;
    margin-top: 4px;
  }
  .contact-list {
    position: absolute;
    left: 250px;
    top: 112px;
    list-style: none;
    font-family: "Open Sans", sans-serif;
    font-size: 14px;
    color: var(--ink-grey);
  }
  .contact-list__item {
    display: flex;
    align-items: center;
    gap: 10px;
    margin-bottom: 26px;
    letter-spacing: 0.03em;
  }
  .contact-list__icon { width: 18px; height: 18px; flex: none; }
  .card-back {
    display: flex;
    align-items: center;
    justify-content: center;
  }
  .card-back .wordmark {
    color: var(--brand-blue);
    font-size: 32px;
    letter-spacing: 0.02em;
    text-align: left;
  }
  .card-back .wordmark .wordmark__sub {
    display: block;
    font-size: 15px;
    letter-spacing: 0.42em;
    margin-top: 6px;
  }
</style>
</head>
<body>
  <section class="card card-front" aria-label="Business card front">
    <svg class="card-front__panel" viewBox="0 0 560 342" aria-hidden="true">
      <path d="M0 0 H240 L214 118 Q234 150 212 192 L176 342 H0 Z" fill="var(--brand-blue)"/>
    </svg>
    <div class="wordmark">Tarrow<span class="wordmark__sub">Construct Works</span></div>
    <ul class="contact-list">
      <li class="contact-list__item">
        <svg class="contact-list__icon" viewBox="0 0 18 18" aria-hidden="true"><rect x="5" y="1.5" width="8" height="15" rx="1.5" fill="none" stroke="var(--brand-blue)" stroke-width="1.6"/><line x1="8" y1="14" x2="10" y2="14" stroke="var(--brand-blue)" stroke-width="1.4"/></svg>
        <span>0472 913 046</span>
      </li>
      <li class="contact-list__item">
        <svg class="contact-list__icon" viewBox="0 0 18 18" aria-hidden="true"><rect x="1.5" y="4" width="15" height="10" fill="var(--brand-blue)"/><path d="M1.5 4 L9 10 L16.5 4" fill="none" stroke="#fff" stroke-width="1.2"/></svg>
        <span>admin@tarrowconstructworks.com.au</span>
      </li>
      <li class="contact-list__item">
        <svg class="contact-list__icon" viewBox="0 0 18 18" aria-hidden="true"><g fill="none" stroke="var(--brand-blue)" stroke-width="1.3"><circle cx="9" cy="9" r="7.5"/><ellipse cx="9" cy="9" rx="3.3" ry="7.5"/><line x1="1.5" y1="9" x2="16.5" y2="9"/><line x1="9" y1="1.5" x2="9" y2="16.5"/></g></svg>
        <span>www.tarrowconstructworks.com.au</span>
      </li>
    </ul>
  </section>

  <section class="card card-back" aria-label="Business card back">
    <div class="wordmark">Tarrow<span class="wordmark__sub">Construct Works</span></div>
  </section>
</body>
</html>
```